Business acrd and Stationery desgin FOR HARLOW

I want creative and expressive stationary design .on the front side for business card I need the logo and doctors name to be there and on the back side I need time and appointment .Please see attached business card to use same names ,but use address below and phone number

Note:the deigner must submit the file in vector format and PSD and PDF

Business name is :Harlow Crest Medical Clinic.

Address:
20485 57 ST NW
City :EDMONTON AB
Postal code: T6K 3P8

Phone :(780) 492-3815
Fax:(780) 492-5127

Other Business name :Harlow Medical Clinic

• logo in the back on business card

```html
<!DOCTYPE html>
<html lang="en">
<head>
<meta charset="utf-8">
<title>Harlow Crest Medical Clinic – Business Card</title>
<link rel="stylesheet" href="https://fonts.googleapis.com/css2?family=Crimson+Text:wght@400;600;700&family=Inter:wght@400&display=swap">
<style>
  :root {
    --navy: #2b3c8e;
    --red: #d9262c;
    --grey: #4f4f4f;
    --border: #8a8a8a;
    --orange: rgba(224, 102, 77, 0.38);
    --purple: rgba(79, 79, 151, 0.34);
    --sky: rgba(140, 198, 234, 0.42);
    --paper: #ffffff;
  }
  * { margin: 0; padding: 0; box-sizing: border-box; }
  html, body { width: 1200px; height: 900px; overflow: hidden; background: var(--paper); }
  .sheet { position: relative; width: 1200px; height: 900px; font-family: "Crimson Text", Georgia, serif; }
  .card {
    position: absolute; top: 286px; width: 528px; height: 306px;
    border: 1px solid var(--border); background: var(--paper); overflow: hidden;
  }
  .card--front { left: 51px; }
  .card--back { left: 624px; }
  .ribbon-area { position: absolute; top: 0; right: 0; height: 100%; }
  .card--front .ribbon-area {
    width: 215px;
    background:
      radial-gradient(ellipse 70% 60% at 55% 55%, var(--purple), transparent 75%),
      radial-gradient(ellipse 60% 80% at 70% 35%, var(--orange), transparent 80%),
      radial-gradient(ellipse 60% 40% at 70% 85%, var(--sky), transparent 80%);
  }
  .card--back .ribbon-area {
    width: 255px; height: 270px;
    background:
      radial-gradient(ellipse 60% 55% at 45% 35%, var(--sky), transparent 78%),
      radial-gradient(ellipse 50% 60% at 80% 45%, var(--purple), transparent 80%);
  }
  .brand {
    position: absolute; left: 44px; top: 36px;
    display: flex; align-items: center; gap: 10px;
    color: var(--navy); font-weight: 600; font-size: 19px; line-height: 1.05;
    letter-spacing: 0.04em; text-transform: uppercase;
  }
  .brand__dot { width: 14px; height: 14px; border-radius: 50%; background: var(--red); flex: none; }
  .doctors { position: absolute; left: 44px; top: 114px; color: var(--navy); font-weight: 700; font-size: 19.5px; line-height: 25px; }
  .heading { position: absolute; left: 44px; top: 115px; color: var(--navy); font-weight: 700; font-size: 19.5px; }
  .contact {
    position: absolute; left: 44px; display: grid; grid-template-columns: 141px auto;
    color: var(--grey); font-size: 16.5px; line-height: 19.5px;
  }
  .card--front .contact { top: 188px; }
  .card--back .contact { top: 171px; }
  .contact__label { display: inline-block; width: 35px; }
  .tagline { position: absolute; left: 44px; top: 263px; color: var(--red); font-size: 14px; }
  .blurb { position: absolute; left: 44px; top: 249px; color: var(--navy); font-size: 13.5px; line-height: 17px; }
  .caption { position: absolute; font-family: "Inter", Arial, sans-serif; font-size: 16px; color: #222; }
  .caption--front { left: 296px; top: 630px; }
  .caption--back { left: 877px; top: 630px; }
  .caption--size { left: 542px; top: 708px; }
</style>
</head>
<body>
<main class="sheet">

  <section class="card card--front" aria-label="Front of business card">
    <div class="ribbon-area" role="img" aria-label="Decorative flowing ribbons in coral, violet and sky blue"></div>
    <div class="brand"><span class="brand__dot"></span><span>Harlow Crest<br>Medical Clinic</span></div>
    <div class="doctors">Dr. L. Marchetti<br>Dr. N. Okafor</div>
    <div class="contact">
      <span>20485 57 ST NW</span><span><span class="contact__label">Tel</span>(780) 492-3815</span>
      <span>Edmonton AB</span><span><span class="contact__label">Fax</span>(780) 492-5127</span>
      <span>T6K 3P8</span><span>www.harlowcrestclinic.com</span>
    </div>
    <p class="tagline">Family Doctors • Family Practice &amp; Walk-in Welcome</p>
  </section>

  <section class="card card--back" aria-label="Back of business card">
    <div class="ribbon-area" role="img" aria-label="Decorative flowing ribbons in sky blue and violet"></div>
    <div class="brand"><span class="brand__dot"></span><span>Harlow<br>Medical Clinic</span></div>
    <h2 class="heading">Harlow Walk-in Clinic</h2>
    <div class="contact">
      <span>6190 121 Ave NW</span><span><span class="contact__label">Tel</span>(780) 492-3900</span>
      <span>Edmonton, AB</span><span>info@harlowmedicalclinic.com</span>
      <span>T6K 2R4</span><span>www.harlowmedicalclinic.com</span>
    </div>
    <p class="blurb">Whether you need to see a family doctor, pediatrician or a specialist doctor.<br>Our physicians at our Edmonton medical walk-in clinic provide the best service.</p>
  </section>

  <p class="caption caption--front">Front</p>
  <p class="caption caption--back">Back</p>
  <p class="caption caption--size">9.5cm x 5.5cm</p>

</main>
</body>
</html>
```